10' x 4' outdoor vinyl banner

My company prepare and sell delicious Maryland Style Gourmet Crab Cake sandwiches at public events like fairs, festivals and concerts.
We use a 10' x 10' tent to prepare and sell this sandwiches at those events. I need a 10x4 (10 feet long by 4 feet high) banner display for the top of the tent. The same design should be scalable to another 10x3 banner for the bottom of the tent.
I need a general design of a banner with a wording that should be very attention catching
The wording is: "Maryland Crab Cake Sandwiches"
I would like also to incorporate into the design a blue crab (this is the name of specific type of crab that I'm looking for, is not just a crab painted in blue)
The theme of the design should be the sea, the shoreline, maybe some fishing boat, waves, etc, in that spirit.
I would like to use a nice blue color in the background, as we are talking about the sea and marine themes.
There are some other wordings that I would like to incorporate into the banner:
A Traditional Chesapeake Bay recipe with 100% All Natural, Blue Crab Meat . . . Rich and Flavorful . . .
This type should be in smaller size, but still visible, maybe in italics or an elegant font type.
I want something simple, inviting, like my delicious sandwiches.

```html
<!DOCTYPE html>
<html lang="en">
<head>
<meta charset="utf-8">
<title>Maryland Crab Cake Sandwiches – Tent Banner</title>
<link rel="stylesheet" href="https://fonts.googleapis.com/css2?family=Chango&family=Amatic+SC:wght@700&display=swap">
<style>
  :root {
    --page: #ffffff;
    --sea: #68c5e2;
    --foam: #ffffff;
    --sand: #f0e3a0;
    --pebble: #e2d8c8;
    --title-ink: #302a84;
    --tagline-ink: #1c1c1c;
    --crab-tone-a: #5a6ea8;
    --crab-tone-b: #7a7f8c;
    --shell-tone-a: #d9c4d6;
    --shell-tone-b: #eeaa70;
  }
  html, body {
    margin: 0;
    width: 1200px;
    height: 900px;
    overflow: hidden;
    background: var(--page);
  }
  .canvas {
    position: relative;
    width: 1200px;
    height: 900px;
  }
  .banner {
    position: absolute;
    left: 152px;
    top: 232px;
    width: 894px;
    height: 380px;
    overflow: hidden;
  }
  .banner__scenery {
    position: absolute;
    inset: 0;
    width: 100%;
    height: 100%;
  }
  .banner__title {
    position: absolute;
    left: 0;
    right: 0;
    top: 22px;
    margin: 0;
    text-align: center;
    font-family: "Chango", "Arial Black", sans-serif;
    font-weight: 400;
    color: var(--title-ink);
    font-size: 64px;
    line-height: 88px;
    letter-spacing: -1px;
  }
  .banner__tagline {
    position: absolute;
    left: 0;
    right: 0;
    top: 248px;
    margin: 0;
    text-align: center;
    font-family: "Amatic SC", "Comic Sans MS", cursive;
    font-weight: 700;
    color: var(--tagline-ink);
    font-size: 46px;
    line-height: 64px;
    letter-spacing: 1px;
  }
  .banner__tagline .line { display: block; }
  .banner__tagline .line--first { padding-left: 30px; }
  .illustration {
    position: absolute;
    border-radius: 40%;
  }
  .illustration--crab {
    left: 22px;
    top: 108px;
    width: 180px;
    height: 200px;
    background: radial-gradient(circle at 55% 40%, var(--crab-tone-b), var(--crab-tone-a) 70%, rgba(90,110,168,0) 100%);
  }
  .illustration--shells {
    left: 728px;
    top: 100px;
    width: 160px;
    height: 190px;
    background: radial-gradient(circle at 45% 45%, var(--shell-tone-a), var(--shell-tone-b) 70%, rgba(238,170,112,0) 100%);
  }
</style>
</head>
<body>
<div class="canvas">
  <section class="banner">
    <svg class="banner__scenery" viewBox="0 0 894 380" preserveAspectRatio="none" aria-hidden="true">
      <rect width="894" height="380" fill="var(--sea)"/>
      <path d="M0 160 C 200 205, 520 215, 894 150 L894 380 L0 380 Z" fill="var(--foam)"/>
      <path d="M0 192 C 120 230, 220 238, 300 232 C 360 226, 400 220, 460 226 C 520 232, 600 246, 700 232 C 780 222, 840 224, 894 214 L894 380 L0 380 Z" fill="var(--sand)"/>
      <g fill="var(--pebble)">
        <circle cx="16" cy="182" r="6"/>
        <circle cx="226" cy="212" r="6"/>
        <circle cx="238" cy="224" r="5"/>
        <circle cx="430" cy="218" r="5"/>
        <circle cx="446" cy="232" r="6"/>
        <circle cx="472" cy="222" r="6"/>
        <circle cx="720" cy="206" r="5"/>
        <circle cx="742" cy="230" r="6"/>
      </g>
    </svg>

    <div class="illustration illustration--crab" role="img" aria-label="Illustration of a Chesapeake blue crab with a starfish and seaweed on the sand"></div>
    <div class="illustration illustration--shells" role="img" aria-label="Illustration of seashells and seaweed on the shore"></div>

    <h1 class="banner__title">Maryland Crab Cake<br>Sandwiches</h1>
    <p class="banner__tagline">
      <span class="line line--first">A traditional Chesapeake Bay receipe with</span>
      <span class="line">100% all natural, blue crab meat… rich and flavorful</span>
    </p>
  </section>
</div>
</body>
</html>
```